electrical automation company needs a letterhead design

we need a letter head designed for our new electrical automation company. Our company color are orange and blue as you'll see from our logo attached

Target Market(s)

Domestic, commercial and industrial electrical clients

Industry/Entity Type

Electrical

Contact Information for Business Card

I need to update my business card to make it more eye catching I have attached my old business card designs, logo and new trifold brochure to give you an idea

Font styles to use
Sans Serif

Colors
f37122
0393ce

Requirements
Must have
• larkfield electrical logo
my name
phone number
email
website
Nice to have
• QR code linked to my website
list of some services
- domestic
- commercial
- industrial

```html
<!DOCTYPE html>
<html lang="en">
<head>
<meta charset="utf-8">
<title>Larkfield Electrical – Business Card</title>
<link rel="stylesheet" href="https://fonts.googleapis.com/css2?family=Montserrat:wght@400;500;600;700&display=swap">
<style>
  :root {
    --stage: #1b1b1c;
    --card: #262627;
    --card-edge: #303031;
    --blue: #0393ce;
    --orange: #f37122;
    --silver: #8d8e90;
    --white: #f4f4f4;
  }
  * { box-sizing: border-box; margin: 0; padding: 0; }
  html, body {
    width: 1200px; height: 900px; overflow: hidden;
    background: var(--stage);
    font-family: "Montserrat", sans-serif;
  }
  .stage {
    position: relative; width: 1200px; height: 900px;
    display: flex; flex-direction: column; align-items: center; justify-content: center; gap: 36px;
  }
  .card {
    position: relative; width: 700px; height: 400px;
    background: linear-gradient(135deg, var(--card) 0%, #2c2c2d 55%, var(--card) 100%);
    border: 1px solid var(--card-edge);
    box-shadow: 0 14px 30px rgba(0,0,0,.5);
  }

  /* Front */
  .card--front { display: flex; flex-direction: column; align-items: center; justify-content: center; }
  .front-brand {
    margin-top: 20px;
    font-weight: 600; font-size: 38px; letter-spacing: 2px;
    text-transform: uppercase; color: var(--silver);
  }
  .services {
    position: absolute; bottom: 52px; left: 0; right: 0;
    text-align: center; font-weight: 500; font-size: 19px; letter-spacing: 3px; text-transform: uppercase;
    color: var(--white);
  }
  .services .blue { color: var(--blue); }
  .services .orange { color: var(--orange); }
  .services .sep { margin: 0 10px; }

  /* Back */
  .card--back { display: flex; align-items: center; }
  .back-brand {
    width: 330px; padding-left: 44px;
    font-weight: 600; font-size: 27px; line-height: 1.25; letter-spacing: 1px;
    text-transform: uppercase; color: var(--blue);
  }
  .divider { width: 2px; height: 170px; background: var(--blue); margin-right: 34px; }
  .contact { color: var(--white); }
  .contact__name {
    font-weight: 600; font-size: 40px; letter-spacing: 3px; text-transform: uppercase; color: var(--blue);
    line-height: 1;
  }
  .contact__role { font-size: 19px; font-weight: 500; margin: 4px 0 16px; }
  .contact__list { list-style: none; font-size: 17px; line-height: 1.5; }
  .contact__list li { display: flex; align-items: center; gap: 8px; }
  .contact__list svg { width: 13px; height: 13px; flex: none; }
</style>
</head>
<body>
<main class="stage">
  <section class="card card--front" aria-label="Card front">
    <div class="front-brand">Larkfield Electrical</div>
    <p class="services">
      <span class="blue">Domestic</span><span class="sep">|</span><span class="orange">Commercial</span><span class="sep">|</span><span class="blue">Industrial</span>
    </p>
  </section>

  <section class="card card--back" aria-label="Card back">
    <div class="back-brand">Larkfield Electrical</div>
    <div class="divider"></div>
    <div class="contact">
      <h1 class="contact__name">Owen Tarrant</h1>
      <p class="contact__role">Director</p>
      <ul class="contact__list">
        <li>
          <svg viewBox="0 0 16 16" aria-hidden="true"><path fill="var(--blue)" d="M3.5 1.5l2.5 0 1 3.5-1.6 1.2c.8 1.8 2.2 3.2 4 4l1.2-1.6 3.4 1v2.5c0 .8-.7 1.4-1.5 1.4C6.7 13.5 2.5 9.3 2.1 3c0-.8.6-1.5 1.4-1.5z"/></svg>
          0412 555 018
        </li>
        <li>
          <svg viewBox="0 0 16 16" aria-hidden="true"><rect x="1.5" y="3.5" width="13" height="9" fill="none" stroke="var(--blue)" stroke-width="1.5"/><path d="M1.5 3.5l6.5 5 6.5-5" fill="none" stroke="var(--blue)" stroke-width="1.5"/></svg>
          owen@larkfield-electrical.com.au
        </li>
        <li>
          <svg viewBox="0 0 16 16" aria-hidden="true"><g fill="none" stroke="var(--blue)" stroke-width="1.3"><circle cx="8" cy="8" r="6.3"/><ellipse cx="8" cy="8" rx="2.8" ry="6.3"/><path d="M1.7 8h12.6"/></g></svg>
          www.larkfield-electrical.com.au
        </li>
        <li>
          <svg viewBox="0 0 16 16" aria-hidden="true"><path fill="var(--blue)" d="M8 1a4.7 4.7 0 0 0-4.7 4.7C3.3 9.3 8 15 8 15s4.7-5.7 4.7-9.3A4.7 4.7 0 0 0 8 1zm0 6.5a1.8 1.8 0 1 1 0-3.6 1.8 1.8 0 0 1 0 3.6z"/></svg>
          PO Box 418 Kestrel Bay SA 5799
        </li>
      </ul>
    </div>
  </section>
</main>
</body>
</html>
```